The Quiet Meadow - a modern wellness brand

Looking for a modern, simple, and clean website for a virtual consulting firm focused on holistic wellness and sustainable living. Want a strong combo of text and photos (really shitty starts are available for reference on www.thequietmeadowhub.example and www.ginaposlund.example for reference - general idea is in the right direction, was too difficult to work through with the wordpress template and nothing laid out correctly)
Needs include:
- strong home / landing page
- ability to schedule (use calend.ly) on the site
- online shop / purchasing POS integration
- blog
-multiple 'services' pages
- about page
- contact page
(attached brand board images for brand style / reference)
Updates
Want more opportunity for designs and feedback
Target Market(s)
women and gay men aged 30-50
Coding
Coded - Design and coding required
Number of Pages Required
5+ page
Colors
Designer to choose only greyscale colors for use in the design.
Requirements
Must have
- the ability for me to update and manage through wordpress when things like pricing, or services change
Should not have
- complicated anything

```html
<!DOCTYPE html>
<html lang="en">
<head>
<meta charset="utf-8">
<title>The Quiet Meadow</title>
<link href="https://fonts.googleapis.com/css2?family=Jost:wght@300;400;500&family=Lato:wght@400;700&display=swap" rel="stylesheet">
<style>
:root{
  --ink:#1f1f1f;
  --text:#4a4a4a;
  --muted:#8a8a8a;
  --grey:#7b7b7b;
  --mid:#7d7d7d;
  --line:#d9d9d9;
  --soft:#f4f4f4;
  --white:#ffffff;
  --dark:#2b2b2b;
  --black:#0b0b0b;
}
*{box-sizing:border-box;margin:0;padding:0}
html,body{width:1200px;height:3712px;overflow:hidden}
body{position:relative;font-family:"Lato",sans-serif;color:var(--text);background:var(--white)}
.abs{position:absolute}
h1,h2,h3,h4{font-family:"Jost",sans-serif;font-weight:400;color:var(--ink)}

.topbar{left:0;top:0;width:1200px;height:43px;background:var(--grey);color:var(--white);font-size:13px}
.topbar span{position:absolute;top:13px}
.topbar .sep{top:9px;width:1px;height:26px;background:rgba(255,255,255,.6)}
.topbar .dot{top:16px;width:10px;height:10px;border-radius:50%;background:var(--white)}

.navbar{left:0;top:43px;width:1200px;height:84px;background:var(--white);border-bottom:1px solid var(--line)}
.brand-badge{left:91px;top:22px;width:120px;height:120px;border-radius:50%;background:var(--white);display:flex;align-items:center;justify-content:center;z-index:3}
.brand-name{left:200px;top:64px;font-family:"Jost",sans-serif;font-size:16px;letter-spacing:3px;color:var(--ink);z-index:3;font-weight:400;white-space:nowrap}
.nav-link{top:78px;font-family:"Lato",sans-serif;font-size:15px;color:var(--ink)}
.nav-link.active{color:var(--muted)}
.nav-underline{left:448px;top:124px;width:32px;height:3px;background:var(--grey)}
.btn-pill{display:flex;align-items:center;justify-content:center;border-radius:30px;color:var(--white);font-size:15px;font-family:"Lato",sans-serif}
.btn-call{left:952px;top:65px;width:151px;height:42px;background:var(--mid)}

.hero{left:0;top:127px;width:1200px;height:648px;background:radial-gradient(ellipse at 45% 55%,#8a4e2c 0%,#5a3220 45%,#2b1a12 100%)}
.hero-title{left:0;width:1200px;text-align:center;color:var(--white);font-family:"Jost",sans-serif;font-weight:400}
.hero-title.l1{top:510px;font-size:80px;letter-spacing:14px}
.hero-title.l2{top:606px;font-size:44px;letter-spacing:34px}

.about-photo{left:113px;top:845px;width:440px;height:440px;border-radius:50%;background:radial-gradient(circle at 40% 40%,#4d4845 0%,#2a2624 70%,#1a1716 100%);box-shadow:0 10px 30px rgba(0,0,0,.25)}
.about-title{left:599px;top:862px;font-size:37px}
.about-text{left:599px;top:920px;width:494px;font-size:15.5px;line-height:30px;color:var(--text)}
.btn-shop{left:592px;top:1212px;width:157px;height:54px;background:var(--mid)}

.process{left:0;top:1361px;width:1200px;height:621px;background:var(--soft)}
.section-title{left:0;width:1200px;text-align:center;font-size:37px}
.step{width:206px;text-align:center}
.step h3{font-size:30px;margin-top:0;white-space:nowrap}
.step p{font-size:14.5px;line-height:26px;margin-top:10px;color:var(--text)}

.blog-title{top:2038px}
.card{background:var(--white);border-radius:22px;box-shadow:0 6px 22px rgba(0,0,0,.08);text-align:center}
.card-photo{border-radius:22px}
.date-tag{background:var(--dark);color:var(--white);font-size:13px;border-radius:16px;padding:7px 16px}
.card h4,.card-body h4{font-size:23px;line-height:30px}
.card p,.card-body p{font-size:14.5px;line-height:25px;color:var(--text)}
.card-body p{margin-top:14px}
.learn{font-size:15px;color:var(--muted);display:inline-flex;align-items:center;gap:6px;margin-top:4px}
.learn i{display:inline-block;width:20px;height:14px;border-radius:8px;background:#cfcfcf}
.btn-more{left:532px;top:2615px;width:151px;height:52px;background:var(--dark);font-size:16px}

.contact{left:0;top:2731px;width:1200px;height:506px;background:var(--soft)}
.info-icon{width:50px;height:50px;border-radius:50%;border:1.5px solid var(--muted);display:flex;align-items:center;justify-content:center}
.info-label{font-family:"Jost",sans-serif;font-size:23px;color:var(--ink)}
.info-val{font-size:14.5px;line-height:24px;color:var(--text)}
.field{background:var(--white);color:var(--muted);font-size:14.5px;padding:0 24px;display:flex;align-items:center}
.field.area{align-items:flex-start;padding-top:17px}
.btn-submit{left:429px;top:3093px;width:319px;height:53px;background:var(--dark);color:var(--white);display:flex;align-items:center;justify-content:center;font-size:16px}

.footer{left:0;top:3237px;width:1200px;height:475px;background:var(--black);color:var(--white)}
.footer-name{left:0;width:1200px;text-align:center;font-family:"Jost",sans-serif;font-size:34px;letter-spacing:8px;color:var(--white)}
.footer-links{left:0;width:1200px;display:flex;justify-content:center;gap:44px;font-size:15px;color:var(--white)}
.copy{left:0;width:1200px;text-align:center;font-size:13.5px;color:var(--white)}
.copy u{text-decoration:underline}
.social{width:42px;height:42px;border-radius:50%;background:var(--white)}
.social.first{background:var(--grey)}
</style>
</head>
<body>

<!-- Top bar -->
<div class="abs topbar">
  <svg class="abs" style="left:458px;top:14px" width="14" height="14" viewBox="0 0 24 24"><path fill="#fff" d="M6.6 10.8a15 15 0 006.6 6.6l2.2-2.2c.3-.3.7-.4 1-.2 1.1.4 2.3.6 3.6.6.6 0 1 .4 1 1V20c0 .6-.4 1-1 1A17 17 0 013 4c0-.6.4-1 1-1h3.5c.6 0 1 .4 1 1 0 1.3.2 2.5.6 3.6.1.3 0 .7-.2 1z"/></svg>
  <span style="left:480px">+1 555 010 2040</span>
  <span class="sep" style="left:608px"></span>
  <svg class="abs" style="left:628px;top:15px" width="14" height="11" viewBox="0 0 14 11"><rect width="14" height="11" rx="1" fill="#fff"/><path d="M1 1l6 5 6-5" stroke="#7b7b7b" fill="none"/></svg>
  <span style="left:648px">info@thequietmeadowhub.example</span>
  <span class="sep" style="left:868px"></span>
  <span style="left:890px">&#8594; Login</span>
  <span class="sep" style="left:972px"></span>
  <i class="abs dot" style="left:1003px"></i>
  <i class="abs dot" style="left:1024px"></i>
  <i class="abs dot" style="left:1045px"></i>
  <i class="abs dot" style="left:1066px"></i>
</div>

<!-- Navigation -->
<div class="abs navbar"></div>
<div class="abs brand-badge">
  <svg width="70" height="70" viewBox="0 0 70 70"><circle cx="35" cy="35" r="30" fill="none" stroke="#1f1f1f" stroke-width="1.2"/></svg>
</div>
<div class="abs brand-name">THE QUIET MEADOW</div>
<a class="abs nav-link active" style="left:444px">Home</a>
<a class="abs nav-link" style="left:520px">Online shop</a>
<a class="abs nav-link" style="left:638px">Services</a>
<a class="abs nav-link" style="left:732px">About</a>
<a class="abs nav-link" style="left:809px">Blog</a>
<a class="abs nav-link" style="left:874px">Contact</a>
<div class="abs nav-underline"></div>
<a class="abs btn-pill btn-call">Schedule A Call</a>

<!-- Hero -->
<div class="abs hero" role="img" aria-label="Photograph of a hand brushing through tall meadow grass in warm sunset light"></div>
<h1 class="abs hero-title l1">THE QUIET</h1>
<div class="abs hero-title l2">MEADOW</div>

<!-- About -->
<div class="abs about-photo" role="img" aria-label="Round photograph of an open book and candles in a dim, calm room"></div>
<h2 class="abs about-title">About The Quiet Meadow</h2>
<p class="abs about-text">Lorem ipsum dolor sit amet, consectetur adipiscing elit, sed do eius-mod tempor incididunt ut labore et dolore magna aliqua. Quis ipsum suspendisse ultrices gravida. Risus commodo viverra maecenas ac-cumsan lacus vel facilisis. Lorem ipsum dolor sit amet, consectetur adipiscing elit, sed do eiusmod tempor incididunt ut labore et dolore magna aliqua. Quis ipsum suspendisse ultrices gravida. Risus commo-do viverra maecenas accumsan lacus vel facilisis. Lorem ipsum dolor sit amet, consectetur adipiscing elit, sed do eiusmod tempor incididunt ut labore et dolore magna aliqua.</p>
<a class="abs btn-pill btn-shop">Online shop</a>

<!-- Process -->
<div class="abs process"></div>
<h2 class="abs section-title" style="top:1420px">Our Process</h2>

<svg class="abs" style="left:0;top:1480px" width="1200" height="240" viewBox="0 1480 1200 240">
  <g fill="none" stroke="#8a8a8a" stroke-width="4" stroke-linecap="round" stroke-dasharray="0 9">
    <circle cx="213" cy="1596" r="99"/>
    <circle cx="470" cy="1596" r="99"/>
    <circle cx="727" cy="1596" r="99"/>
    <circle cx="985" cy="1596" r="99"/>
  </g>
  <g fill="#7d7d7d">
    <circle cx="213" cy="1596" r="86"/>
    <circle cx="470" cy="1596" r="86"/>
    <circle cx="727" cy="1596" r="86"/>
    <circle cx="985" cy="1596" r="86"/>
  </g>
  <g fill="#2b2b2b">
    <circle cx="249" cy="1675" r="29"/>
    <circle cx="506" cy="1675" r="29"/>
    <circle cx="763" cy="1675" r="29"/>
    <circle cx="1021" cy="1675" r="29"/>
  </g>
  <g fill="#fff" font-family="Jost, sans-serif" font-size="16" text-anchor="middle">
    <text x="249" y="1672">01</text><text x="249" y="1692">Step</text>
    <text x="506" y="1672">02</text><text x="506" y="1692">Step</text>
    <text x="763" y="1672">03</text><text x="763" y="1692">Step</text>
    <text x="1021" y="1672">04</text><text x="1021" y="1692">Step</text>
  </g>
</svg>
<div class="abs" role="img" aria-label="Line icon of a person with a lightbulb" style="left:173px;top:1556px;width:80px;height:80px"></div>
<div class="abs" role="img" aria-label="Line icon of a thinking head with a pencil" style="left:430px;top:1556px;width:80px;height:80px"></div>
<div class="abs" role="img" aria-label="Line icon of documents with an idea and a pencil" style="left:687px;top:1556px;width:80px;height:80px"></div>
<div class="abs" role="img" aria-label="Line icon of a blueprint with a ruler and pencil" style="left:945px;top:1556px;width:80px;height:80px"></div>

<div class="abs step" style="left:115px;top:1717px"><h3>Understand</h3><p>Always remember in the jungle there’s a lot of them in there, after you overcome them, you will make it to paradise.</p></div>
<div class="abs step" style="left:373px;top:1717px"><h3>Imagine</h3><p>You see the hedges, how I got it shaped up? It’s im-portant to shape up your hedges, it’s like getting a haircut, stay fresh.</p></div>
<div class="abs step" style="left:626px;top:1717px"><h3>Create</h3><p>We don’t see them, we will never see them. To be suc-cessful you’ve got to work hard, to make history, simple, you’ve got to make it.</p></div>
<div class="abs step" style="left:887px;top:1717px"><h3>Build</h3><p>Look at the sunset. Sur-round yourself with angels, positive energy, beautiful people, beautiful souls, clean heart, angel.</p></div>

<!-- Blog -->
<h2 class="abs section-title blog-title">Recent Blog</h2>

<div class="abs card" style="left:109px;top:2240px;width:310px;height:336px"></div>
<div class="abs card-photo" role="img" aria-label="Photograph of a woman in white sitting cross-legged with a hand on her chest" style="left:128px;top:2125px;width:274px;height:238px;background:linear-gradient(135deg,#d8cfc6,#efeae6 50%,#b9a79a)"></div>
<div class="abs date-tag" style="left:145px;top:2141px">OCT 31, 2022</div>
<div class="abs card-body" style="left:115px;top:2380px;width:298px;text-align:center">
  <h4>Lorem ipsum dolor sit amet, consectetur adipiscing</h4>
  <p>Lorem ipsum dolor sit amet, consecte-tur adipiscing elit</p>
  <span class="learn">Learn More <i></i></span>
</div>

<div class="abs card" style="left:447px;top:2240px;width:308px;height:336px"></div>
<div class="abs card-photo" role="img" aria-label="Photograph of stacked grey stones on raked sand" style="left:464px;top:2125px;width:274px;height:238px;background:radial-gradient(circle at 55% 55%,#8c8c8c 0%,#c9bfb3 40%,#e6ddd2 100%)"></div>
<div class="abs date-tag" style="left:481px;top:2141px">OCT 31, 2022</div>
<div class="abs card-body" style="left:452px;top:2380px;width:298px;text-align:center">
  <h4>Lorem ipsum dolor sit amet, consectetur adipiscing</h4>
  <p>Lorem ipsum dolor sit amet, consecte-tur adipiscing elit</p>
  <span class="learn">Learn More <i></i></span>
</div>

<div class="abs card" style="left:776px;top:2123px;width:310px;height:219px;padding:24px 14px 0">
  <h4>Lorem ipsum dolor sit amet, consectetur adipiscing elit, sed do</h4>
  <p style="margin-top:8px">Lorem ipsum dolor sit amet, consecte-tur adipiscing eliti</p>
  <span class="learn">Learn More <i></i></span>
</div>
<div class="abs card" style="left:776px;top:2357px;width:310px;height:219px;padding:24px 14px 0">
  <h4>Lorem ipsum dolor sit amet, consectetur adipiscing</h4>
  <p style="margin-top:8px">Lorem ipsum dolor sit amet, consecte-tur adipiscing elit, sed do eiusmod tempor incididunt ut</p>
  <span class="learn">Learn More <i></i></span>
</div>

<a class="abs btn-pill btn-more">View More</a>

<!-- Contact -->
<div class="abs contact"></div>
<h2 class="abs section-title" style="top:2788px;left:-10px">Conatct Us</h2>

<div class="abs info-icon" style="left:106px;top:2889px">
  <svg width="16" height="20" viewBox="0 0 16 20"><path d="M8 1a6 6 0 00-6 6c0 5 6 12 6 12s6-7 6-12a6 6 0 00-6-6z" fill="none" stroke="#7b7b7b" stroke-width="1.6"/><circle cx="8" cy="7" r="2" fill="#7b7b7b"/></svg>
</div>
<div class="abs info-label" style="left:171px;top:2882px">Location</div>
<div class="abs info-val" style="left:171px;top:2918px;width:250px">112/b The Quiet Meadow sit amet, consectetur adipiscing</div>

<div class="abs info-icon" style="left:106px;top:3001px">
  <svg width="16" height="16" viewBox="0 0 24 24"><path fill="#7b7b7b" d="M6.6 10.8a15 15 0 006.6 6.6l2.2-2.2c.3-.3.7-.4 1-.2 1.1.4 2.3.6 3.6.6.6 0 1 .4 1 1V20c0 .6-.4 1-1 1A17 17 0 013 4c0-.6.4-1 1-1h3.5c.6 0 1 .4 1 1 0 1.3.2 2.5.6 3.6.1.3 0 .7-.2 1z"/></svg>
</div>
<div class="abs info-label" style="left:171px;top:2994px">Phone</div>
<div class="abs info-val" style="left:171px;top:3030px">+1 555 010 2040</div>

<div class="abs info-icon" style="left:106px;top:3089px">
  <svg width="16" height="13" viewBox="0 0 14 11"><rect width="14" height="11" rx="1" fill="#7b7b7b"/><path d="M1 1l6 5 6-5" stroke="#fff" fill="none"/></svg>
</div>
<div class="abs info-label" style="left:171px;top:3082px">Email</div>
<div class="abs info-val" style="left:171px;top:3118px">info@thequietmeadowhub.example</div>

<div class="abs field" style="left:429px;top:2888px;width:319px;height:52px">Name</div>
<div class="abs field" style="left:429px;top:2956px;width:319px;height:52px">Phone</div>
<div class="abs field" style="left:429px;top:3024px;width:319px;height:52px">Email</div>
<div class="abs btn-submit">Submit</div>
<div class="abs field area" style="left:766px;top:2888px;width:319px;height:258px">Type your message</div>

<!-- Footer -->
<div class="abs footer"></div>
<svg class="abs" style="left:550px;top:3285px" width="100" height="100" viewBox="0 0 100 100"><circle cx="50" cy="50" r="46" fill="none" stroke="#fff" stroke-width="1.5"/></svg>
<div class="abs footer-name" style="top:3402px">THE QUIET MEADOW</div>
<div class="abs footer-links" style="top:3498px"><span>Terms &amp; conditions</span><span>Privacy Policy</span><span>About Us</span><span>Support</span></div>
<div class="abs copy" style="top:3553px">Copyright© 2022 &nbsp;<u>The Quiet Meadow</u> &nbsp;| &nbsp;All Rights Reserved</div>
<div class="abs social first" style="left:502px;top:3605px"></div>
<div class="abs social" style="left:552px;top:3605px"></div>
<div class="abs social" style="left:604px;top:3605px"></div>
<div class="abs social" style="left:656px;top:3605px"></div>

</body>
</html>
```